Velvet Marlow Ent Presents Gold fringe n swing

I'm looking to create a flyer for my event which is on April 15 2017 and night club event themed red lips in hitPresented by VelvitMarlow entertainment.Host by rswbk dree valcourt.Special appearance bronzo tha champ Music by dj kestrel. The TwirlBelles will be in the building to give you the entertainment your eye would enjoy Etc.
9pm 2am $25 before 12 Dress to Impress/ Dress code enforced Tight Security Bottle Service/ Hookahs Available RSVP for VIP/ Birthdays.
Contacts Dusty 555-318-0742 Rex 555-462-9158
Jolene 555-207-5863.CadillacJoeEntertainment@gmail.comApril 15 2017Cadillac Joe Presents Gold Fringe N Swing Host by RSWBK Vixen Dree Valcourt
they request not to promote, performance or Live for flyer.
Address.
KVR@The Parlor7
488-36 Harlan T Pruitt Ave
Philadelphia PA 19387

Target Market(s)

Club Flyer

Industry/Entity Type

Night Club

Font styles to use
Decorative

Requirements
Must have
• Must be design in the target for nightlife club event.
• The uploads has the names saved as who they are.
• possible to set up as 4x6 printable flyer double sided
• and 8.5x11 for poster can complete different.
• https://velvetmarlowentertainment.ticketorchard.net
• 21&up
Nice to have
• Neat and sexy to appeal to the eye.

```html
<!DOCTYPE html>
<html lang="en">
<head>
<meta charset="utf-8">
<title>Gold Fringe N Swing – Club Flyer</title>
<link href="https://fonts.googleapis.com/css2?family=Archivo+Black&family=Oswald:wght@400;500;600&family=Great+Vibes&family=Open+Sans:wght@400;600;700&display=swap" rel="stylesheet">
<style>
:root{
  --bg:#6b6b6b;
  --ink:#161616;
  --ink-2:#262626;
  --pink:#ff1d8e;
  --pink-deep:#c4005f;
  --magenta:#d63cc8;
  --violet:#8a2bd1;
  --white:#ffffff;
  --grey:#d9d9d9;
}
*{margin:0;padding:0;box-sizing:border-box}
html,body{width:1200px;height:1200px;overflow:hidden;background:var(--bg)}
.stage{position:relative;width:1200px;height:1200px}
.flyer{position:absolute;top:199px;width:536px;height:803px;background:var(--ink);overflow:hidden;
  font-family:"Open Sans",sans-serif;color:var(--white)}
.flyer--front{left:62px}
.flyer--back{left:603px}

/* front */
.glow-band{position:absolute;left:0;right:0;top:70px;height:500px;
  background:linear-gradient(90deg,var(--violet) 0%,var(--magenta) 35%,var(--pink) 70%,#ff4a4a 100%);opacity:.85}
.glow-band::after{content:"";position:absolute;inset:0;background:linear-gradient(180deg,rgba(22,22,22,.2),rgba(22,22,22,0) 40%,rgba(22,22,22,.9) 100%)}
.host-photo{position:absolute;left:34px;top:41px;width:464px;height:432px;border-radius:50% 50% 8px 8px/60% 60% 8px 8px;
  background:radial-gradient(ellipse at 50% 65%,var(--pink) 0%,#a0105a 35%,#2a2a2a 75%)}
.brand-mark{position:absolute;display:flex;align-items:center;gap:6px;font-family:"Oswald",sans-serif;font-weight:600;text-transform:uppercase;color:var(--white)}
.brand-mark--partner{left:30px;top:50px;font-size:17px;width:110px;line-height:1.1}
.brand-mark--client{right:22px;top:60px;font-size:16px;width:140px;line-height:1.1}
.brand-mark .dot{flex:none;width:16px;height:16px;background:var(--pink)}
.brand-mark .ring{flex:none;width:18px;height:18px;border-radius:50%;background:var(--white)}
.date-badge{position:absolute;left:22px;top:325px;width:168px;height:168px;border-radius:50%;
  background:var(--ink);border:5px solid var(--pink);box-shadow:0 0 0 3px var(--ink),0 0 0 6px var(--pink-deep);
  text-align:center;padding-top:18px}
.date-badge .month{font-family:"Great Vibes",cursive;font-size:40px;line-height:1;color:var(--white)}
.date-badge .day{font-family:"Oswald",sans-serif;font-size:35px;font-weight:500;line-height:1.1;color:var(--pink);letter-spacing:-1px;white-space:nowrap}
.date-badge .time{font-family:"Oswald",sans-serif;font-size:24px;line-height:1.3;color:var(--white)}
.age-badge{position:absolute;left:415px;top:429px;width:88px;height:88px;border-radius:50%;background:var(--pink-deep);text-align:center;padding-top:8px}
.age-badge .age{font-family:"Oswald",sans-serif;font-size:40px;font-weight:500;line-height:1}
.age-badge .note{font-family:"Oswald",sans-serif;font-size:11px}
.presents{position:absolute;left:150px;top:476px;font-size:19px;font-weight:700;text-transform:uppercase;letter-spacing:-.5px;white-space:nowrap}
.presents span{font-weight:400}
.title{font-family:"Archivo Black",sans-serif;text-transform:uppercase;color:var(--pink);line-height:1;letter-spacing:-2px;white-space:nowrap;
  text-shadow:0 3px 0 var(--pink-deep),0 6px 12px rgba(0,0,0,.8)}
.title-ring{position:absolute;border-radius:50%;background:radial-gradient(circle,#a0105a 0%,#6a0a3d 70%)}
.flyer--front .title-ring{left:20px;top:562px;width:126px;height:126px}
.flyer--front .title-line-1{position:absolute;left:60px;top:505px;font-size:62px}
.flyer--front .title-line-2{position:absolute;left:34px;top:578px;font-size:100px}
.host-line{position:absolute;left:34px;top:708px;font-size:24px;font-weight:600;letter-spacing:-.5px;white-space:nowrap}
.host-line .script{font-family:"Great Vibes",cursive;font-size:32px;font-weight:400;margin-right:6px}
.venue{position:absolute;left:58px;top:752px;display:flex;align-items:center;gap:14px}
.venue .name{font-size:28px;font-weight:700;letter-spacing:-1px;white-space:nowrap}
.venue .address{font-size:13px;font-weight:600;line-height:1.4;text-transform:uppercase;white-space:nowrap}

/* back */
.top-glow{position:absolute;left:0;right:0;top:0;height:100px;background:linear-gradient(90deg,#ff5a6a,var(--pink) 40%,var(--magenta) 80%,var(--violet))}
.top-glow::after{content:"";position:absolute;inset:0;background:linear-gradient(180deg,transparent 40%,var(--ink))}
.guest-photo{position:absolute;left:0;top:0;width:157px;height:257px;background:linear-gradient(160deg,#8a1a24,#c8846a 55%,#3a2a2a)}
.flyer--back .title-ring{left:138px;top:145px;width:100px;height:100px}
.flyer--back .title-line-1{position:absolute;left:165px;top:82px;font-size:46px}
.flyer--back .title-line-2{position:absolute;left:150px;top:150px;font-size:76px}
.guests{position:absolute;left:0;right:0;top:265px;height:216px;background:var(--ink-2)}
.guest{position:absolute;top:0;height:216px}
.guest--one{left:0;width:273px;background:linear-gradient(135deg,#8ec9ea,#f2f2f2 70%);clip-path:polygon(0 0,100% 0,88% 100%,0 100%)}
.guest--two{left:245px;width:291px;background:linear-gradient(135deg,#3b3b3b,#e9651d 60%,#9c3d10);clip-path:polygon(12% 0,100% 0,100% 100%,0 100%)}
.appearance{position:absolute;left:196px;top:265px;width:176px;height:50px;background:var(--white);clip-path:polygon(0 0,100% 0,90% 100%,10% 100%);text-align:center;z-index:2}
.appearance .script{position:absolute;left:0;right:0;top:-2px;font-family:"Great Vibes",cursive;font-size:20px;line-height:1;color:var(--ink)}
.appearance .label{position:absolute;left:0;right:0;top:16px;font-family:"Oswald",sans-serif;font-size:28px;font-weight:500;color:var(--pink);line-height:1}
.name-tag{position:absolute;top:454px;height:27px;background:var(--pink);font-family:"Oswald",sans-serif;font-size:16px;font-weight:500;line-height:27px;padding:0 10px 0 16px;text-transform:uppercase;white-space:nowrap;clip-path:polygon(8% 0,100% 0,100% 100%,0 100%);z-index:2}
.name-tag--guest{right:300px}
.name-tag--dj{left:258px}
.name-tag .script{font-family:"Great Vibes",cursive;font-size:18px;text-transform:none;margin-right:4px}
.dancer-photo{position:absolute;left:325px;top:481px;width:211px;height:322px;background:linear-gradient(180deg,#f2f2f2,#cfcfcf 40%,#3a2a2a)}
.perks{position:absolute;left:20px;top:520px;font-family:"Oswald",sans-serif;font-size:24px;font-weight:500;line-height:1.38;color:var(--pink);text-transform:uppercase;letter-spacing:-.8px;white-space:nowrap;z-index:1}
.rule{position:absolute;left:20px;width:310px;border-top:2px dotted var(--grey)}
.rule--top{top:622px}
.rule--bottom{top:752px}
.rsvp{position:absolute;left:20px;top:630px;font-size:16px;letter-spacing:-.3px}
.contacts{position:absolute;left:20px;top:652px;font-size:26px;line-height:1.2;letter-spacing:-1px;font-weight:400;white-space:nowrap}
.contacts b{font-weight:600}
.email{position:absolute;left:22px;top:760px;font-size:14px;color:var(--pink);white-space:nowrap}
.crew-badge{position:absolute;left:278px;top:595px;width:112px;height:112px;border-radius:50%;background:var(--white);border:4px solid var(--pink);text-align:center;color:var(--ink);padding-top:8px;z-index:2}
.crew-badge .script{font-family:"Great Vibes",cursive;font-size:24px;line-height:.9}
.crew-badge .name{font-family:"Oswald",sans-serif;font-size:18px;font-weight:500;color:var(--pink);line-height:1.05;letter-spacing:-.5px}
.crew-badge .note{font-size:11px;font-weight:700;font-style:italic;line-height:1.15}
</style>
</head>
<body>
<div class="stage">

  <section class="flyer flyer--front">
    <div class="glow-band"></div>
    <div class="host-photo" role="img" aria-label="Photo of the host in a pink dress"></div>
    <div class="brand-mark brand-mark--partner"><span class="dot"></span>TwirlBelles Ent</div>
    <div class="brand-mark brand-mark--client"><span class="ring"></span>Velvet Marlow Ent</div>

    <div class="date-badge">
      <div class="month">April</div>
      <div class="day">15TH, 2017</div>
      <div class="time">9PM 2AM</div>
    </div>
    <div class="age-badge">
      <div class="age">21+</div>
      <div class="note">ID ENFORCED</div>
    </div>

    <div class="presents">Velvet Marlow <span>Presents</span></div>
    <div class="title-ring"></div>
    <div class="title title-line-1">Gold Fringe</div>
    <div class="title title-line-2">N Swing</div>

    <div class="host-line"><span class="script">Host by</span>RSWBK Vixen Dree Valcourt</div>
    <div class="venue">
      <div class="name">KVR @ PARLOR7</div>
      <div class="address">488-36 Harlan T Pruitt Ave<br>Philadelphia PA 19387</div>
    </div>
  </section>

  <section class="flyer flyer--back">
    <div class="top-glow"></div>
    <div class="guest-photo" role="img" aria-label="Photo of the host with red hair"></div>
    <div class="title-ring"></div>
    <div class="title title-line-1">Gold Fringe</div>
    <div class="title title-line-2">N Swing</div>

    <div class="guests">
      <div class="guest guest--one" role="img" aria-label="Photo of special guest Bronzo Tha Champ"></div>
      <div class="guest guest--two" role="img" aria-label="Photo of DJ Kestrel"></div>
    </div>
    <div class="appearance"><span class="script">Special</span><span class="label">APPEARANCE</span></div>
    <div class="name-tag name-tag--guest">Bronzo Tha Champ</div>
    <div class="name-tag name-tag--dj"><span class="script">Music by</span>DJ Kestrel</div>

    <div class="dancer-photo" role="img" aria-label="Photo of a dancer in black lace"></div>

    <div class="perks">25$ Before 12 // Dress Code Enforced<br>Tight Security // Bottle Service<br>Hookahs Available</div>
    <div class="rule rule--top"></div>
    <div class="rsvp">RSVP for VIP/ Birthdays Contacts</div>
    <div class="contacts">REX <b>555-462-9158</b><br>DUSTY <b>555-318-0742</b><br>JOLENE <b>555-207-5863</b></div>
    <div class="rule rule--bottom"></div>
    <div class="email">VelvetMarlowEntertainment@brindlepost.net</div>

    <div class="crew-badge">
      <div class="script">The</div>
      <div class="name">TWIRLBELLES</div>
      <div class="note">will be in the<br>Building</div>
    </div>
  </section>

</div>
</body>
</html>
```